Web Design for non-profit, Nautical themed

We are developing a web design for a non-profit organization. They are:

a non-profit 501©3 educational and service organization, grounded in the recognition that active engagement of the arts through can be an entry into growth and transformation. Our purpose is to develop and offer events that support this creative process bringing outstanding presenters to our town.

They are located in a beautiful coastal town and the client would like a "nautical" theme. This would include

- color palette of blue, green, possibly brown/beige, and possibly some deep red colors as accents. There is a file attached with some color palette ideas, but you don't have to choose from colors here.

- soothing, calm, clean professional look

- something in the background image that would indicate the four directions. This could be a compass or something similar.

- the client really likes this website:
http://www.harbrowcollective.example/

Please see attached for:

- a basic sketch that shows the overall layout that we desire. Feel free to modify this slightly but not too much. File name is 01-sketch.psd

- placeholder content that can be used throughout your design

You can also use any of the stock photos found here:
http://www.pellumimages.example/search/lightbox/48207356#b9a2d71

Target Market(s)

Mainly white American women who are in their 40s or older. Professional, affluent, highly educated.

Industry/Entity Type

Nautical

Requirements
Must have
• - sidebar with event information. Each event should include date, headshot, title, brief description and a "Register" and "Read more" link. We don't have any real headshots so use ones from Internet for now.

- use the attached 01-sketch.psd file as your starting point.

```html
<!DOCTYPE html>
<html lang="en">
<head>
<meta charset="utf-8">
<title>Harborlight Dialogues INC.</title>
<link rel="stylesheet" href="https://fonts.googleapis.com/css2?family=Roboto+Condensed:wght@400;700&family=Arimo:wght@400&display=swap">
<style>
:root{
  --teal:#0e7390;
  --navy:#0b2347;
  --slate:#7393ae;
  --slate-line:#5f7f9a;
  --footer:#374a5a;
  --footer-line:#2e4452;
  --cyan:#25b6d6;
  --text:#666;
  --heading:#1c3a5c;
  --white:#fff;
}
*{margin:0;padding:0;box-sizing:border-box}
html,body{width:1200px;height:1040px;overflow:hidden}
body{position:relative;background:linear-gradient(#e9e9e9,#fbfbfb 60%,#fff);font-family:"Arimo",Arial,sans-serif;color:var(--text)}

.main-nav{position:absolute;left:0;top:0;width:1200px;height:50px;background:var(--teal);border-bottom:3px solid var(--footer-line)}
.main-nav a{position:absolute;top:0;height:47px;line-height:47px;color:var(--white);text-decoration:none;font-family:"Roboto Condensed",Arial,sans-serif;font-size:16px;transform:translateX(-50%);white-space:nowrap}
.main-nav a.active{left:120px;width:113px;text-align:center;transform:none;top:4px;height:43px;line-height:40px;background:linear-gradient(#4d5f6e,#2f4050)}

.brand{position:absolute;left:120px;top:100px;display:flex;align-items:center;gap:12px}
.brand-mark{width:40px;height:40px;background:#555}
.brand-name{font-family:"Roboto Condensed",Arial,sans-serif;font-size:30px;color:#333;line-height:1}
.call{position:absolute;right:119px;top:88px;font-family:"Roboto Condensed",Arial,sans-serif;font-size:18px;color:var(--teal)}
.search{position:absolute;left:829px;top:138px;width:252px;height:37px;border:1px solid #ddd;background:#f2f2f2}
.search .btn{position:absolute;right:0;top:0;width:37px;height:35px;border-left:1px solid #ddd}

.sidebar{position:absolute;left:120px;top:204px;width:300px;height:694px;background:var(--slate)}
.social{display:flex;gap:14px;justify-content:center;padding-top:12px;height:60px}
.social span{width:36px;height:36px;display:block}
.fb{background:#3b5bb0}.tw{background:#2fb8ec}.gp{background:#d8382c}.yt{background:#d0141b}
.mailing{background:var(--navy);height:117px;padding:20px 10px 0 12px}
.mailing h2{font-family:"Roboto Condensed",Arial,sans-serif;font-weight:400;font-size:23px;color:var(--white)}
.mailing .row{display:flex;gap:6px;margin-top:17px}
.mailing .field{width:208px;height:31px;background:var(--white);border:1px solid #ccc}
.mailing .signup{width:64px;height:31px;background:linear-gradient(#7fa0bb,#5d7f9c);color:var(--white);font-family:"Roboto Condensed",Arial,sans-serif;font-size:14px;text-align:center;line-height:29px;border:1px solid #9ab}
.events-title{font-family:"Roboto Condensed",Arial,sans-serif;font-weight:400;font-size:23px;color:var(--white);padding:13px 10px 0;height:50px;border-bottom:1px solid var(--slate-line)}
.event{height:141px;border-bottom:1px solid var(--slate-line);padding:9px 10px 0 11px}
.event .date{font-size:13px;color:#e8eef4}
.event h3{font-weight:400;font-size:13.5px;color:var(--navy);margin-top:3px}
.event .body{display:flex;gap:10px;margin-top:9px}
.event .photo{width:70px;height:70px;flex:none}
.event p{font-size:11.5px;line-height:14.5px;color:var(--white);text-align:justify;hyphens:manual}
.view-all{position:absolute;right:10px;bottom:10px;width:84px;height:28px;background:linear-gradient(#7fa0bb,#5d7f9c);border:1px solid #9ab;color:var(--white);font-family:"Roboto Condensed",Arial,sans-serif;font-size:14px;text-align:center;line-height:26px}

.hero{position:absolute;left:440px;top:204px;width:640px;height:330px;background:linear-gradient(#4c57a8 0%,#6b6fb8 35%,#3a3a55 65%,#2a2526 100%)}
.dots{position:absolute;left:271px;bottom:2px;width:96px;height:18px;border-radius:9px 9px 0 0;background:rgba(120,120,120,.7);display:flex;gap:3px;align-items:center;justify-content:center}
.dots i{width:10px;height:10px;border-radius:50%;background:#ccc;display:block}
.dots i.on{background:#333}
.intro{position:absolute;left:438px;top:544px;width:643px}
.intro h1{font-family:"Roboto Condensed",Arial,sans-serif;font-weight:400;font-size:22px;color:var(--heading)}
.intro p{font-size:12px;line-height:18px;margin-top:10px;letter-spacing:-.06px;text-align:justify}

.card{position:absolute;top:649px;width:200px;height:249px;background:var(--teal)}
.card h2{font-family:"Roboto Condensed",Arial,sans-serif;font-size:19px;font-weight:400;color:var(--white);height:45px;line-height:40px;padding-left:10px;border-bottom:1px solid #2a8aa4;letter-spacing:.3px}
.card p{font-size:12px;line-height:14.5px;color:var(--white);padding:0 6px;text-align:justify;margin-top:10px;letter-spacing:-.2px}
.card p+p{margin-top:14px}
.card .more{position:absolute;left:52px;bottom:5px;width:86px;height:28px;background:linear-gradient(#2aa7c8,#13809e);border:1px solid #4bb9d4;color:var(--white);font-family:"Roboto Condensed",Arial,sans-serif;font-size:13px;text-align:center;line-height:26px}

.site-footer{position:absolute;left:0;top:918px;width:1200px;height:122px;background:var(--footer);color:var(--white);font-size:12px}
.site-footer h4{font-weight:400;font-size:12px;color:var(--cyan);position:absolute;top:18px}
.site-footer .line{position:absolute;display:flex;align-items:center;gap:8px}
.site-footer .social2{position:absolute;left:850px;top:63px;display:flex;gap:14px}
.site-footer .social2 span{width:36px;height:36px;display:block}
</style>
</head>
<body>
<nav class="main-nav">
  <a class="active" href="#">HOME</a>
  <a href="#" style="left:316px">CALENDAR</a>
  <a href="#" style="left:471px">ABOUT US</a>
  <a href="#" style="left:618px">DONATE</a>
  <a href="#" style="left:805px">TRAVEL INFORMATION</a>
  <a href="#" style="left:1005px">CONTACT</a>
</nav>

<div class="brand"><span class="brand-mark"></span><span class="brand-name">Harborlight Dialogues INC.</span></div>
<div class="call">CALL US: 1 800 555 0142</div>
<div class="search"><div class="btn">
  <svg width="37" height="35" viewBox="0 0 37 35"><circle cx="17" cy="15" r="4" fill="none" stroke="#bbb" stroke-width="1.5"/><line x1="20" y1="18" x2="24" y2="22" stroke="#bbb" stroke-width="2"/></svg>
</div></div>

<aside class="sidebar">
  <div class="social">
    <span class="fb" role="img" aria-label="Social network link"></span>
    <span class="tw" role="img" aria-label="Social network link"></span>
    <span class="gp" role="img" aria-label="Social network link"></span>
    <span class="yt" role="img" aria-label="Video channel link"></span>
  </div>
  <div class="mailing">
    <h2>JOIN OUR MAILING LIST</h2>
    <div class="row"><div class="field"></div><div class="signup">SIGNUP</div></div>
  </div>
  <h2 class="events-title">UPCOMING EVENTS</h2>
  <div class="event">
    <div class="date">JUNE 05, 2013</div>
    <h3>At veroaccusamus et iusto odio dignissimos</h3>
    <div class="body"><div class="photo" role="img" aria-label="Headshot of speaker" style="background:linear-gradient(#e8e4dc,#8a6a50)"></div>
    <p>At vero eos et accusamus et iusto odio dignissimos ducimus qui blan&shy;ditiis praesentium voluptatum deleniti atque corrupti quos dolores et quas molestias excepturi sint occaecati</p></div>
  </div>
  <div class="event">
    <div class="date">JUNE 05, 2013</div>
    <h3>At veroaccusamus et iusto odio dignissimos</h3>
    <div class="body"><div class="photo" role="img" aria-label="Headshot of speaker" style="background:linear-gradient(#f0ece6,#c08a5a)"></div>
    <p>At vero eos et accusamus et iusto odio dignissimos ducimus qui blan&shy;ditiis praesentium voluptatum deleniti atque corrupti quos dolores et quas molestias excepturi sint occaecati</p></div>
  </div>
  <div class="event">
    <div class="date">JUNE 05, 2013</div>
    <h3>At veroaccusamus et iusto odio dignissimos</h3>
    <div class="body"><div class="photo" role="img" aria-label="Group of people at an event" style="background:linear-gradient(#dfe3e6,#6c7580)"></div>
    <p>At vero eos et accusamus et iusto odio dignissimos ducimus qui blan&shy;ditiis praesentium voluptatum deleniti atque corrupti quos dolores et quas molestias excepturi sint occaecati</p></div>
  </div>
  <div class="view-all">VIEW ALL</div>
</aside>

<div class="hero" role="img" aria-label="Evening street in a coastal town with lamp posts and historic buildings">
  <div class="dots"><i></i><i></i><i class="on"></i><i></i><i></i><i></i></div>
</div>

<section class="intro">
  <h1>Conversations that Could Transform Your Life</h1>
  <p>Lorem ipsum dolor sit amet, consectetur adipisicing elit, sed do eiusmod tempor incididunt ut labore et dolore magna aliqua. Ut enim ad minim veniam, quis nostrud exercitation ullamco laboris nisi ut aliquip ex ea commodo consequat. Duis aute irure dolor in reprehenderit in voluptate velit esse cillum d</p>
</section>

<section class="card" style="left:440px">
  <h2>&gt; ABOUT US</h2>
  <p>Lorem ipsum dolor sit amet, consectetur adipisicing elit, sed do eiusmod tempor incididunt ut labore et dolore magna aliqua.</p>
  <p>Ut enim ad minim veniam, quis nostrud exercitation ullamco laboris nisi ut aliquip ex ea commodo consequat. Duis aute irure dolor in reprehenderitesse cillum</p>
  <div class="more">READ MORE</div>
</section>
<section class="card" style="left:660px">
  <h2>&gt; OUR SPEAKERS</h2>
  <p>Lorem ipsum dolor sit amet, consectetur adipisicing elit, sed do eiusmod tempor incididunt ut labore et dolore magna aliqua.</p>
  <p>Ut enim ad minim veniam, quis nostrud exercitation ullamco laboris nisi ut aliquip ex ea commodo consequat. Duis aute irure dolor in reprehenderitesse cillum</p>
  <div class="more">READ MORE</div>
</section>
<section class="card" style="left:880px">
  <h2>&gt; ANNAPOLIS</h2>
  <p>Lorem ipsum dolor sit amet, consectetur adipisicing elit, sed do eiusmod tempor incididunt ut labore et dolore magna aliqua.</p>
  <p>Ut enim ad minim veniam, quis nostrud exercitation ullamco laboris nisi ut aliquip ex ea commodo consequat. Duis aute irure dolor in reprehenderitesse cillum</p>
  <div class="more">READ MORE</div>
</section>

<footer class="site-footer">
  <h4 style="left:119px">SITEMAP</h4>
  <div class="line" style="left:120px;top:51px">Home | Calendar | About Us | Donate | Travel Information | Contact</div>
  <div class="line" style="left:120px;top:81px">©2013 Harborlight Dialogues INC..</div>

  <h4 style="left:539px">CONTACT US</h4>
  <div class="line" style="left:541px;top:45px">
    <svg width="14" height="14" viewBox="0 0 14 14"><path d="M7 1a4 4 0 0 1 4 4c0 3-4 8-4 8S3 8 3 5a4 4 0 0 1 4-4z" fill="#aab"/><circle cx="7" cy="5" r="1.5" fill="#374a5a"/></svg>
    18 Quayside Ave, Port Elden, USA</div>
  <div class="line" style="left:541px;top:69px">
    <svg width="14" height="14" viewBox="0 0 14 14"><path d="M2 1h3l1 3-2 1c1 2 2 3 4 4l1-2 3 1v3c-6 0-10-4-10-10z" fill="#aab"/></svg>
    1 800 555 0142</div>
  <div class="line" style="left:541px;top:93px">
    <svg width="14" height="14" viewBox="0 0 14 14"><rect x="1" y="3" width="12" height="8" fill="#aab"/><path d="M1 3l6 5 6-5" fill="none" stroke="#374a5a"/></svg>
    info@harborlight.example</div>

  <h4 style="left:850px">FOLLOW US</h4>
  <div class="social2">
    <span class="fb" role="img" aria-label="Social network link"></span>
    <span class="tw" role="img" aria-label="Social network link"></span>
    <span class="gp" role="img" aria-label="Social network link"></span>
    <span class="yt" role="img" aria-label="Video channel link"></span>
  </div>
</footer>
</body>
</html>
```